11 x 11 Flyer Design for Social Media - Reverse Mortgages

62 or older?

A Reverse Mortgage
could be
Your Road to Financial Freedom

* No Monthly Payments
* No Income Requirements
* No Credit Score Requirements
* No Loss of Ownership

Receive cash by lump sum, monthly installments or a line of credit!!

Call us today for a Free Consultation!!
(800) 647-2915

Harborline Financial Services, Inc.
NMLS #517830
www.harborlinefunds.example

```html
<!DOCTYPE html>
<html lang="en">
<head>
<meta charset="utf-8">
<title>Reverse Mortgage Flyer</title>
<link rel="stylesheet" href="https://fonts.googleapis.com/css2?family=Roboto:wght@400;500;700;900&family=Arimo:wght@400;700&display=swap">
<style>
  :root {
    --blue-deep: #14618f;
    --blue-bright: #2a90d2;
    --green: #a7cf3a;
    --ink: #2f2f2f;
    --paper: #ffffff;
    --mist: #eef0f2;
  }
  * { margin: 0; padding: 0; box-sizing: border-box; }
  html, body { width: 1200px; height: 1200px; overflow: hidden; background: var(--paper); }
  .flyer { position: relative; width: 1200px; height: 1200px; overflow: hidden; font-family: "Roboto", sans-serif; }

  .hero-photo {
    position: absolute; left: 0; top: 0; width: 1200px; height: 836px;
    background:
      linear-gradient(90deg, #ffffff 0%, #f7f9fa 28%, rgba(247,249,250,0) 55%),
      linear-gradient(180deg, #dfe7ec 0%, #c7d4dc 40%, #d9dee2 75%, #e4e6e8 100%);
  }

  .headline {
    position: absolute; left: 72px; top: 82px;
    font-weight: 700; font-size: 118px; line-height: 104px; letter-spacing: -1px;
    background: linear-gradient(90deg, var(--blue-deep) 0%, var(--blue-bright) 70%);
    -webkit-background-clip: text; background-clip: text; color: transparent;
  }
  .subhead {
    position: absolute; left: 72px; top: 309px;
    font-weight: 500; font-size: 42px; line-height: 54px; color: var(--ink);
  }

  .benefit-band { position: absolute; left: 0; top: 0; width: 1200px; height: 836px; }

  .benefits { position: absolute; left: 0; top: 620px; width: 1200px; height: 216px; }
  .benefit {
    position: absolute; top: 0; width: 260px; height: 200px; text-align: center;
    font-size: 23px; line-height: 29px; color: var(--ink);
  }
  .benefit svg { display: block; margin: 42px auto 14px; }
  .benefit-divider { position: absolute; top: 8px; width: 1px; height: 186px; background: #9fb8c8; }

  .cash-band {
    position: absolute; left: 0; top: 836px; width: 1200px; height: 115px;
    background: var(--green); color: #fff; text-align: center;
    font-weight: 700; font-size: 33px; line-height: 43px; padding-top: 15px;
    font-family: "Arimo", sans-serif;
  }
  .cta { position: absolute; left: 0; top: 951px; width: 1200px; height: 170px; text-align: center; font-family: "Arimo", sans-serif; }
  .cta-lead { margin-top: 30px; font-weight: 700; font-size: 31px; color: #222; }
  .cta-phone { margin-top: 0; font-weight: 700; font-size: 72px; line-height: 86px; color: var(--blue-deep); }

  .footer {
    position: absolute; left: 0; top: 1121px; width: 1200px; height: 79px;
    background: linear-gradient(90deg, var(--blue-deep) 0%, var(--blue-bright) 50%, var(--blue-deep) 100%);
    color: #fff; font-family: "Arimo", sans-serif; font-size: 26px;
    display: flex; align-items: center; justify-content: space-between; padding: 0 48px 0 44px;
  }
  .footer-item { display: flex; align-items: center; gap: 12px; }
</style>
</head>
<body>
<main class="flyer">
  <div class="hero-photo" role="img" aria-label="Photo of a smiling senior couple dressed in white on a beach"></div>

  <h1 class="headline">62 OR<br>OLDER?</h1>
  <p class="subhead">A Reverse Mortgage<br>could be<br>Your Road to Financial<br>Freedom</p>

  <svg class="benefit-band" viewBox="0 0 1200 836" aria-hidden="true">
    <defs>
      <linearGradient id="benefitFill" x1="0" y1="0" x2="0" y2="1">
        <stop offset="0" stop-color="#f4f5f6"/>
        <stop offset="1" stop-color="#e9ebed"/>
      </linearGradient>
    </defs>
    <path d="M0 725 Q600 335 1200 700 L1200 836 L0 836 Z" fill="url(#benefitFill)"/>
    <path d="M0 752 Q600 380 1200 768" fill="none" stroke="var(--green)" stroke-width="5"/>
    <path d="M0 728 Q600 340 1200 703" fill="none" stroke="var(--blue-bright)" stroke-width="22"/>
  </svg>

  <section class="benefits">
    <div class="benefit" style="left:56px">
      <svg width="70" height="76" viewBox="0 0 70 76" fill="var(--blue-deep)" aria-hidden="true">
        <rect x="22" y="4" width="22" height="34" rx="2" transform="rotate(-12 33 21)"/>
        <rect x="34" y="2" width="22" height="34" rx="2" fill="var(--blue-bright)" transform="rotate(10 45 19)"/>
        <rect x="24" y="32" width="34" height="30" rx="8"/>
        <rect x="4" y="44" width="18" height="28" rx="2"/>
      </svg>
      No Monthly<br>Payments
    </div>
    <div class="benefit-divider" style="left:321px"></div>
    <div class="benefit" style="left:331px">
      <svg width="76" height="76" viewBox="0 0 76 76" fill="var(--blue-bright)" aria-hidden="true">
        <circle cx="34" cy="26" r="13"/>
        <circle cx="56" cy="10" r="9" fill="var(--blue-deep)"/>
        <path d="M4 52 Q20 44 36 54 L56 50 Q66 48 70 42 L72 48 Q62 66 36 68 Q16 68 4 60 Z" fill="var(--blue-deep)"/>
      </svg>
      No Income<br>Requirements
    </div>
    <div class="benefit-divider" style="left:594px"></div>
    <div class="benefit" style="left:603px">
      <svg width="86" height="70" viewBox="0 0 86 70" aria-hidden="true">
        <rect x="2" y="6" width="62" height="44" rx="3" fill="var(--blue-bright)"/>
        <rect x="8" y="20" width="34" height="4" fill="#fff"/>
        <rect x="8" y="30" width="26" height="4" fill="#fff"/>
        <path d="M50 14 H84 V66 L78 62 L72 66 L66 62 L60 66 L54 62 L50 66 Z" fill="var(--blue-deep)"/>
        <text x="67" y="50" text-anchor="middle" font-family="Roboto, sans-serif" font-weight="700" font-size="28" fill="#fff">$</text>
      </svg>
      No Credit Score<br>Requirements
    </div>
    <div class="benefit-divider" style="left:868px"></div>
    <div class="benefit" style="left:879px">
      <svg width="72" height="72" viewBox="0 0 72 72" aria-hidden="true">
        <path d="M18 34 L40 14 L62 34 V56 H18 Z" fill="var(--blue-bright)"/>
        <circle cx="40" cy="36" r="6" fill="#fff"/>
        <circle cx="16" cy="12" r="8" fill="var(--blue-deep)"/>
        <rect x="8" y="50" width="14" height="20" fill="var(--blue-deep)"/>
        <path d="M22 58 Q40 50 60 58 L62 66 H22 Z" fill="var(--blue-deep)"/>
      </svg>
      No Loss of<br>Ownership
    </div>
  </section>

  <div class="cash-band">RECEIVE CASH BY LUMP SUM, MONTHLY INSTALLMENTS OR<br>A LINE OF CREDIT!!</div>

  <section class="cta">
    <p class="cta-lead">CALL US TODAY FOR A FREE CONSULTATION!!</p>
    <p class="cta-phone">(800) 647-2915</p>
  </section>

  <footer class="footer">
    <span class="footer-item">
      <svg width="18" height="22" viewBox="0 0 18 22" aria-hidden="true"><path d="M9 1 C4 1 1 5 1 9 C1 14 9 21 9 21 C9 21 17 14 17 9 C17 5 14 1 9 1 Z" fill="none" stroke="#fff" stroke-width="2"/><circle cx="9" cy="9" r="3" fill="#fff"/></svg>
      Harborline Financial Services, Inc. NMLS #517830
    </span>
    <span class="footer-item">
      <svg width="22" height="22" viewBox="0 0 22 22" fill="none" stroke="#fff" stroke-width="1.8" aria-hidden="true"><circle cx="11" cy="11" r="9"/><ellipse cx="11" cy="11" rx="4" ry="9"/><path d="M2 11 H20 M4 6 H18 M4 16 H18"/></svg>
      www.harborlinefunds.example
    </span>
  </footer>
</main>
</body>
</html>
```